User Interface Designer Needed

I need a few designs for a property law comparison website. We assist the public with finding a solicitor for the purchase or sale of their house and units. We are currently in the process of creating a questionnaire based woo commerce product filter using gravity forms. I'd like to see designs that use the logo colours. Users will be selecting options such as "Buying" or "Selling", they will then be selecting options such as "House" "Unit" or "Land". Details attached. The final design should communicate ease and simplicity. Questions will be answered one at a time, and the next question is dependent on the answer to the question prior

Target Market(s)

First home buyers, people from ages 18-80 make and female looking to get rid of the hassle of ringing around and going from website to website trying to get a quote

Industry/Entity Type

Real Estate

Number of Pages Required

1 page

Colors
33a6d7

Requirements
Must have
• A design for every question
Nice to have
• Simple symbols or simplistic pictures incorporated, even better if you can turn the question into a picture instead of words eg. A picture of a house, a picture of a unit and a picture of land instead of written answers

```html
<!DOCTYPE html>
<html lang="en">
<head>
<meta charset="utf-8">
<title>Tervo Property Lawyers – Client Details</title>
<link href="https://fonts.googleapis.com/css2?family=Open+Sans:wght@400;600;700&family=Raleway:wght@500;600;700;800&display=swap" rel="stylesheet">
<style>
  :root {
    --brand-blue: #33a6d7;
    --nav-blue: #1fa3da;
    --accent-green: #5fbf1e;
    --text-dark: #3a3a3a;
    --text-muted: #6a6a6a;
    --rule: #e3e3e3;
    --radio-off: #c9c9c9;
    --radio-fill: #f4f4f4;
    --footer-bg: #333333;
    --footer-text: #dddddd;
    --back-grey: #bdbdbd;
    --white: #ffffff;
  }
  * { box-sizing: border-box; margin: 0; padding: 0; }
  html, body { width: 1200px; height: 2311px; overflow: hidden; background: var(--white); }
  body { position: relative; font-family: "Open Sans", Arial, sans-serif; color: var(--text-dark); }

  .top-strip { position: absolute; left: 0; top: 0; width: 1200px; height: 4px; background: var(--brand-blue); }

  .site-header { position: absolute; left: 0; top: 4px; width: 1200px; height: 90px; }
  .brand { position: absolute; left: 99px; top: 26px; display: flex; align-items: center; gap: 10px; }
  .brand-dot { width: 40px; height: 40px; border-radius: 50%; background: var(--brand-blue); }
  .brand-name { font-family: "Raleway", Arial, sans-serif; font-weight: 700; font-size: 34px; color: var(--brand-blue); letter-spacing: -0.5px; }
  .utility-links { position: absolute; right: 99px; top: 38px; display: flex; gap: 10px; align-items: center; font-family: "Raleway", Arial, sans-serif; font-weight: 600; font-size: 12.5px; color: #555; }
  .utility-links span.sep { color: #999; }
  .utility-links svg { vertical-align: -2px; margin-right: 6px; }

  .main-nav { position: absolute; left: 0; top: 94px; width: 1200px; height: 49px; background: var(--nav-blue); }
  .nav-item { position: absolute; top: 16px; font-family: "Raleway", Arial, sans-serif; font-weight: 700; font-size: 14px; color: var(--white); }
  .nav-item.active { color: var(--accent-green); }
  .nav-item.active::after { content: ""; position: absolute; left: 50%; bottom: -17px; margin-left: -7px; border: 7px solid transparent; border-bottom-color: var(--accent-green); border-top: 0; }
  .search-box { position: absolute; left: 744px; top: 5px; width: 357px; height: 40px; background: var(--white); border-radius: 3px; }
  .search-box span { position: absolute; left: 17px; top: 12px; font-size: 12px; color: #999; }
  .search-box svg { position: absolute; right: 14px; top: 11px; }

  .hero { position: absolute; left: 0; top: 143px; width: 1200px; height: 330px;
    background: linear-gradient(180deg, #7fa9d9 0%, #b8cfe6 35%, #a7b98a 55%, #8fae45 75%, #a6a84a 100%); }
  .hero-kicker, .hero-title { position: absolute; width: 100%; text-align: center; font-family: "Raleway", Arial, sans-serif; font-weight: 800; color: var(--white); text-shadow: 0 2px 4px rgba(0,0,0,0.35); }
  .hero-kicker { top: 62px; font-size: 32px; letter-spacing: 1px; }
  .hero-title { top: 110px; font-size: 46px; letter-spacing: 1px; }
  .hero-cta { position: absolute; left: 514px; top: 183px; width: 173px; height: 48px; background: var(--accent-green); border: 2px solid var(--white); color: var(--white); font-family: "Raleway", Arial, sans-serif; font-weight: 700; font-size: 17px; text-align: center; line-height: 44px; }
  .hero-arrow { position: absolute; top: 146px; width: 38px; height: 38px; border-radius: 50%; background: rgba(40,40,40,0.7); }
  .hero-arrow svg { position: absolute; left: 12px; top: 11px; }
  .hero-dots { position: absolute; left: 557px; top: 276px; display: flex; gap: 4px; }
  .hero-dots i { display: block; width: 20px; height: 20px; border-radius: 50%; border: 2px solid var(--white); }
  .hero-dots i.on { background: var(--accent-green); }

  .form-title { position: absolute; left: 99px; top: 516px; font-family: "Raleway", Arial, sans-serif; font-weight: 700; font-size: 20px; color: var(--text-dark); }
  .form-title-rule { position: absolute; left: 99px; top: 564px; width: 1002px; height: 5px; background: var(--brand-blue); }

  .question-label { position: absolute; left: 99px; font-size: 16px; color: var(--text-muted); }
  .divider { position: absolute; left: 99px; width: 1002px; height: 1px; background: var(--rule); }

  .option { position: absolute; left: 100px; display: flex; align-items: flex-start; font-family: "Open Sans", Arial, sans-serif; font-weight: 600; font-size: 13px; line-height: 22px; color: #444; text-transform: uppercase; }
  .option .radio { flex: none; width: 22px; height: 22px; border-radius: 50%; border: 2px solid var(--radio-off); background: var(--radio-fill); margin-right: 23px; position: relative; }
  .option.selected { color: var(--accent-green); }
  .option.selected .radio { border-color: var(--accent-green); background: var(--white); }
  .option.selected .radio::after { content: ""; position: absolute; left: 4px; top: 4px; width: 10px; height: 10px; border-radius: 50%; background: var(--accent-green); }
  .option.sub { left: 158px; font-size: 11px; }
  .option.sub .radio { width: 18px; height: 18px; margin-right: 14px; margin-top: 2px; }

  .form-actions { position: absolute; top: 2099px; height: 39px; }
  .btn { position: absolute; top: 0; height: 39px; border-radius: 3px; color: var(--white); font-family: "Open Sans", Arial, sans-serif; font-weight: 700; font-size: 12px; text-align: center; line-height: 39px; }
  .btn-back { left: 838px; width: 80px; background: var(--back-grey); border: 1px solid #aaa; }
  .btn-edit { left: 927px; width: 82px; background: var(--nav-blue); }
  .btn-edit svg { vertical-align: -2px; margin-right: 8px; }
  .btn-finish { left: 1019px; width: 82px; background: var(--accent-green); }

  .site-footer { position: absolute; left: 0; top: 2198px; width: 1200px; height: 113px; background: var(--footer-bg); }
  .footer-brand { position: absolute; left: 99px; top: 38px; display: flex; align-items: center; gap: 9px; }
  .footer-brand .brand-dot { width: 34px; height: 34px; background: var(--white); }
  .footer-brand .brand-name { font-size: 28px; color: var(--white); }
  .footer-links { position: absolute; left: 0; width: 1180px; top: 33px; text-align: center; font-size: 12px; color: var(--footer-text); }
  .footer-links .sep { margin: 0 6px; }
  .copyright { position: absolute; left: 0; width: 1180px; top: 60px; text-align: center; font-size: 12px; color: var(--footer-text); }
  .social { position: absolute; left: 930px; top: 40px; display: flex; gap: 11px; }
  .social i { display: block; width: 30px; height: 30px; border-radius: 4px; background: var(--white); }
</style>
</head>
<body>
  <div class="top-strip"></div>

  <header class="site-header">
    <div class="brand"><span class="brand-dot"></span><span class="brand-name">tervo.com.au</span></div>
    <nav class="utility-links">
      <span><svg width="11" height="12" viewBox="0 0 11 12"><circle cx="5.5" cy="3.5" r="3" fill="#666"/><path d="M0 12c0-4 2.5-5 5.5-5s5.5 1 5.5 5z" fill="#666"/></svg>ADMINISTRATION</span><span class="sep">|</span>
      <span><svg width="12" height="12" viewBox="0 0 12 12"><circle cx="6" cy="6" r="6" fill="#666"/><text x="6" y="9.5" font-size="9" font-weight="700" text-anchor="middle" fill="#fff" font-family="Arial">?</text></svg>HELP</span><span class="sep">|</span>
      <span><svg width="10" height="12" viewBox="0 0 10 12"><rect x="0" y="5" width="10" height="7" fill="#666"/><path d="M2 5V3.5a3 3 0 0 1 6 0V5" fill="none" stroke="#666" stroke-width="1.6"/></svg>LOGIN</span><span class="sep">|</span>
      <span><svg width="12" height="12" viewBox="0 0 12 12"><path d="M1 11l1-3 7-7 2 2-7 7z" fill="#666"/></svg>REGISTER</span>
    </nav>
  </header>

  <nav class="main-nav">
    <span class="nav-item active" style="left:99px">HOME</span>
    <span class="nav-item" style="left:183px">ABOUT US</span>
    <span class="nav-item" style="left:300px">SERVICES</span>
    <span class="nav-item" style="left:411px">NEW CHECK-IN</span>
    <span class="nav-item" style="left:562px">CONTACT US</span>
    <div class="search-box"><span>SEARCH..</span>
      <svg width="17" height="17" viewBox="0 0 17 17"><circle cx="7" cy="7" r="5.5" fill="none" stroke="#888" stroke-width="2.2"/><path d="M11 11l5 5" stroke="#888" stroke-width="2.6"/></svg>
    </div>
  </nav>

  <section class="hero" role="img" aria-label="Photograph of rolling green hills under a blue sky">
    <div class="hero-kicker">TERVO</div>
    <div class="hero-title">PROPERTY LAWYERS</div>
    <div class="hero-cta">GET STARTED</div>
    <div class="hero-arrow" style="left:33px"><svg width="14" height="16" viewBox="0 0 14 16"><path d="M10 2L4 8l6 6" fill="none" stroke="#fff" stroke-width="2.6"/></svg></div>
    <div class="hero-arrow" style="left:1130px"><svg width="14" height="16" viewBox="0 0 14 16"><path d="M4 2l6 6-6 6" fill="none" stroke="#fff" stroke-width="2.6"/></svg></div>
    <div class="hero-dots"><i class="on"></i><i></i><i></i><i></i></div>
  </section>

  <main class="client-form">
    <h2 class="form-title">CLIENT DETAILS</h2>
    <div class="form-title-rule"></div>

    <p class="question-label" style="top:604px">Iam a</p>
    <div class="option selected" style="top:650px"><span class="radio"></span>Buyer</div>
    <div class="option" style="top:693px"><span class="radio"></span>Seller</div>
    <div class="option" style="top:736px"><span class="radio"></span>Buyer and Seller</div>
    <div class="divider" style="top:798px"></div>

    <p class="question-label" style="top:837px">I'm Buying a</p>
    <div class="option selected" style="top:882px"><span class="radio"></span>House</div>
    <div class="option" style="top:925px"><span class="radio"></span>Unit</div>
    <div class="option" style="top:969px"><span class="radio"></span>Land</div>
    <div class="option" style="top:1012px"><span class="radio"></span>House and Land Package</div>
    <div class="divider" style="top:1072px"></div>

    <p class="question-label" style="top:1109px">I would like</p>
    <div class="option selected" style="top:1155px"><span class="radio"></span>Only the searches I need</div>
    <div class="option" style="top:1198px"><span class="radio"></span>Standard Searches</div>
    <div class="option" style="top:1241px"><span class="radio"></span>Premium Searches</div>
    <div class="option" style="top:1284px"><span class="radio"></span><span>I don't need searches included in my quote –<br>I'll pay for searches later at cost</span></div>
    <div class="divider" style="top:1371px"></div>

    <div class="option selected" style="top:1421px"><span class="radio"></span><span>I want my quote to include<br>unlimited extensions</span></div>
    <div class="option" style="top:1491px"><span class="radio"></span><span>I only want to pay<br>for extensions if I need them</span></div>
    <div class="divider" style="top:1577px"></div>

    <div class="option selected" style="top:1618px"><span class="radio"></span>I have signed a contract</div>
    <div class="option" style="top:1688px"><span class="radio"></span>I haven't signed a contract yet</div>
    <div class="divider" style="top:1749px"></div>

    <p class="question-label" style="top:1788px">Risk</p>
    <div class="option selected" style="top:1834px"><span class="radio"></span><span>I want my quote to allow<br>for the possibility of</span></div>
    <div class="option" style="top:1903px"><span class="radio"></span>Terminations</div>
    <div class="option sub" style="top:1945px"><span class="radio"></span>Deed of Recissions</div>
    <div class="option sub" style="top:1980px"><span class="radio"></span>Deed of Variations</div>
    <div class="divider" style="top:2048px"></div>

    <div class="form-actions">
      <span class="btn btn-back">&lt;&lt; BACK</span>
      <span class="btn btn-edit"><svg width="11" height="11" viewBox="0 0 12 12"><path d="M1 11l1-3 7-7 2 2-7 7z" fill="#fff"/></svg>EDIT</span>
      <span class="btn btn-finish">FINISH</span>
    </div>
  </main>

  <footer class="site-footer">
    <div class="footer-brand"><span class="brand-dot"></span><span class="brand-name">tervo.com.au</span></div>
    <p class="footer-links">Help<span class="sep">|</span>FAQ<span class="sep">|</span>Cookies<span class="sep">|</span>Terms &amp; conditions<span class="sep">|</span>Privacy Policy</p>
    <p class="copyright">Copyright © 2016, Tervo - All Rights Reserved</p>
    <div class="social"><i></i><i></i><i></i><i></i></div>
  </footer>
</body>
</html>
```